Corvella Paintless Dent Removal

Our company works on vehicles removing dents using a highly skilled trade which the metal is massaged out with special tools without disturbing the original paint, hence paintless dent removal. Besides keeping the paint and metal original its also very environmentally friendly since no paint or toxic fillers are used. Also we we are one of the most experienced companies in the business with 25 years

Target Market(s)

Retail Automobile consumers, Auto Dealerships and Auto Body Shops

Industry/Entity Type

Auto Repair

Contact Information for Business Card

Dennis Holbrook
PO Box 538 Ashmere, NY 11952
631-472-8816
corvellapdr@mailnest.example
website corvellapdr.example
youtube corvella paintless dent removal
25 years of experience removing Dents, Dings and Hail Damage

Font styles to use
Serif
Sans Serif

Colors

Designer to choose colors to be used in the design.

Requirements
Must have
• I do like things that are simple but classy and somewhat bold, also I like my logo so that should be somewhat important

```html
<!DOCTYPE html>
<html lang="en">
<head>
<meta charset="UTF-8">
<title>Corvella Paintless Dent Removal — Business Card</title>
<link rel="stylesheet" href="https://fonts.googleapis.com/css2?family=Arimo:wght@400;700&family=Tinos:wght@700&display=swap">
<style>
  :root {
    --navy: #021859;
    --lime: #7cfc0a;
    --white: #ffffff;
    --page: #ffffff;
  }
  html, body {
    margin: 0;
    padding: 0;
    width: 1200px;
    height: 1200px;
    overflow: hidden;
    background: var(--page);
  }
  .business-card {
    position: absolute;
    left: 175px;
    top: 365px;
    width: 850px;
    height: 470px;
  }
  .business-card svg { display: block; width: 100%; height: 100%; }
  .fill-navy { fill: var(--navy); }
  .fill-lime { fill: var(--lime); }
  .fill-white { fill: var(--white); }
  .contact-line {
    font-family: "Arimo", Arial, sans-serif;
    font-size: 27px;
    fill: var(--white);
  }
  .brand-name {
    font-family: "Arimo", Arial, sans-serif;
    font-weight: 700;
    fill: var(--navy);
  }
  .holder-name {
    font-family: "Tinos", "Times New Roman", serif;
    font-weight: 700;
    font-size: 50px;
    fill: var(--white);
  }
  .icon-stroke {
    fill: none;
    stroke: var(--white);
    stroke-width: 5;
    stroke-linejoin: round;
  }
</style>
</head>
<body>
  <div class="business-card">
    <svg viewBox="0 0 1063 587" xmlns="http://www.w3.org/2000/svg" aria-label="Corvella Paintless Dent Removal business card for Dennis Holbrook">
      <!-- header band -->
      <rect class="fill-navy" x="0" y="0" width="1063" height="104"/>
      <!-- pinstripe band -->
      <rect class="fill-navy" x="0" y="109" width="1063" height="62"/>
      <rect class="fill-lime" x="0" y="109" width="1063" height="3"/>
      <rect class="fill-lime" x="0" y="129" width="1063" height="3"/>
      <rect class="fill-lime" x="0" y="150" width="1063" height="3"/>
      <!-- contact band -->
      <rect class="fill-navy" x="0" y="254" width="1063" height="170"/>

      <!-- brand plaque -->
      <g class="brand-plaque">
        <rect class="fill-white" x="343" y="240" width="373" height="86"/>
        <ellipse class="fill-white" cx="531" cy="252" rx="218" ry="102"/>
        <text class="brand-name" x="531" y="262" text-anchor="middle" font-size="46">Corvella</text>
        <text class="brand-name" x="531" y="292" text-anchor="middle" font-size="18">Paintless Dent Removal</text>
      </g>

      <!-- contact line -->
      <text class="contact-line" x="131" y="402">PO Box 538 Ashmere</text>
      <text class="contact-line" x="511" y="402">NY 11952</text>
      <text class="contact-line" x="718" y="402">631 - 472 - 8816</text>

      <!-- wave footer -->
      <path class="fill-lime" d="M3 475 C 120 452 300 450 530 472 C 700 486 900 494 1063 475 L1063 524 L3 524 Z"/>
      <path class="fill-navy" d="M530 472 C 700 452 900 448 1063 475 L1063 491 C 900 496 700 488 530 472 Z"/>
      <rect class="fill-navy" x="0" y="524" width="1063" height="63"/>

      <!-- phone and mail icons -->
      <g class="contact-icons">
        <path class="icon-stroke" d="M88 480 L88 488 M80 490 L104 490 Q110 490 110 496 L110 512 M96 512 L96 560 L88 560 Q80 560 80 552 L80 498 Q80 490 88 490"/>
        <rect class="icon-stroke" x="100" y="515" width="62" height="46"/>
        <path class="icon-stroke" d="M100 515 L131 542 L162 515"/>
      </g>

      <text class="holder-name" x="987" y="532" text-anchor="end">Dennis Holbrook</text>
    </svg>
  </div>
</body>
</html>
```